Business / Discount Card

Looking to create a 2 sided business card. Front side to say "Thanks for flying with Skyward Drifts" then have link to "In-Flight Photos, www.skywarddrifts-example.com.au, password: skyward" Back side of card to have company logo, phone number, facebook & instagram logo and #skywarddrifts. Also included on this side will be discount text "Book again and save 10%. Use discount code: skyward10"Round Corner Card Templates are attached. Please ensure dimensions are correct.Thanks,

Font styles to use
Sans Serif

Colors
33a6d7
ffffff
000000

Requirements
Must have
• Logo
• Blue, White and Black color scheme

```html
<!DOCTYPE html>
<html lang="en">
<head>
<meta charset="utf-8">
<title>Skyward Drifts – Business / Discount Card</title>
<link href="https://fonts.googleapis.com/css2?family=Montserrat:ital,wght@0,400;0,500;0,600;0,800;1,800&family=Great+Vibes&display=swap" rel="stylesheet">
<style>
  :root {
    --backdrop: #12506b;
    --sky-blue: #22a9e1;
    --white: #ffffff;
    --black: #000000;
    --ink: #111111;
  }
  html, body { margin: 0; padding: 0; overflow: hidden; }
  body { width: 1200px; height: 1200px; background: var(--backdrop); position: relative; font-family: "Montserrat", sans-serif; }
  .card-shapes { position: absolute; inset: 0; }
  .txt { position: absolute; white-space: nowrap; margin: 0; line-height: 1.2; }
  .center { transform: translateX(-50%); text-align: center; }

  /* Front */
  .front-thanks { left: 564px; top: 272px; font-family: "Great Vibes", cursive; font-size: 36px; color: var(--ink); }
  .front-brand { left: 564px; top: 318px; font-size: 22px; font-weight: 800; letter-spacing: 2.5px; color: var(--sky-blue); text-transform: uppercase; }
  .front-label { left: 564px; top: 381px; font-size: 16px; font-weight: 500; color: var(--ink); }
  .front-url { left: 586px; top: 410px; font-size: 17px; font-weight: 500; color: var(--white); }
  .front-password { left: 564px; top: 442px; font-size: 16px; font-weight: 500; color: var(--ink); }

  /* Back */
  .back-brand { left: 728px; top: 665px; font-size: 44px; font-weight: 800; color: var(--white); }
  .back-phone { left: 603px; top: 776px; font-size: 42px; font-weight: 800; color: var(--sky-blue); }
  .back-social { top: 836px; font-size: 19px; font-weight: 400; color: var(--white); }
  .back-social.facebook { left: 560px; }
  .back-social.instagram { left: 763px; }
  .back-hashtag { left: 728px; top: 875px; font-size: 15px; color: var(--white); }
  .back-offer { left: 582px; top: 909px; font-size: 20px; font-weight: 800; color: var(--white); }
  .back-code { left: 728px; top: 944px; font-size: 15px; color: var(--white); }
</style>
</head>
<body>
  <svg class="card-shapes" width="1200" height="1200" viewBox="0 0 1200 1200">
    <g class="front-card">
      <circle cx="293" cy="280" r="125" fill="var(--white)"/>
      <path d="M168 280 L168 553 L708 553 A70 70 0 0 0 778 483 L778 181 L293 181 Z" fill="var(--white)"/>
      <circle cx="310" cy="330" r="100" fill="var(--sky-blue)" role="img" aria-label="Company logo mark area"/>
      <path d="M409 406 L778 406 L778 437 L409 437 A15.5 15.5 0 0 1 409 406 Z" fill="var(--sky-blue)"/>
    </g>
    <g class="back-card">
      <circle cx="917" cy="727" r="129" fill="var(--black)"/>
      <path d="M411 626 L917 626 L1046 727 L1046 1013 L491 1013 A80 80 0 0 1 411 933 Z" fill="var(--black)"/>
      <g class="phone-icon" fill="none" stroke="var(--white)" stroke-width="3" stroke-linecap="round">
        <path d="M560 794 c-4 4 -2 14 8 24 c10 10 20 12 24 8 l3 -4 l-8 -8 l-5 4 c-4 -2 -10 -8 -12 -12 l4 -5 l-8 -8 z" fill="var(--white)" stroke="none"/>
        <path d="M574 792 a10 10 0 0 1 10 10"/>
        <path d="M576 784 a18 18 0 0 1 16 16"/>
      </g>
      <circle cx="540" cy="849" r="16" fill="var(--sky-blue)"/>
      <circle cx="743" cy="849" r="16" fill="var(--sky-blue)"/>
      <line x1="632" y1="874" x2="826" y2="874" stroke="var(--white)" stroke-width="1"/>
      <line x1="632" y1="895" x2="826" y2="895" stroke="var(--white)" stroke-width="1"/>
      <path d="M539 906 L1046 906 L1046 937 L539 937 A15.5 15.5 0 0 1 539 906 Z" fill="var(--sky-blue)"/>
    </g>
  </svg>

  <p class="txt center front-thanks">Thanks for flying with</p>
  <p class="txt center front-brand">Skyward Drifts</p>
  <p class="txt center front-label">In-Flight Photos</p>
  <p class="txt center front-url">www.skywarddrifts-example.com.au</p>
  <p class="txt center front-password">Password: skyward</p>

  <p class="txt center back-brand">Skyward Drifts</p>
  <p class="txt back-phone">: 1300 SKY FLY</p>
  <p class="txt back-social facebook">skywarddrifts</p>
  <p class="txt back-social instagram">@skywarddrifts</p>
  <p class="txt center back-hashtag">#skywarddrifts</p>
  <p class="txt back-offer">BOOK AGAIN AND SAVE 10%</p>
  <p class="txt center back-code">Use discount code: skyward10</p>
</body>
</html>
```